Website for Excavator and Earthworks Company

We require a modern, sleek and practical website for our newly created earthworks/excavator business in Perth, Western Australia called Gullwind Stonecut Earthworks.

The website should have a modern, cutting edge feel but only needs to be relatively simplistic in it's layout and eventual functionality.

Some pages it should have would be Home, About, Projects and Contact Us.

Number of Pages Required

1 page

```html
<!DOCTYPE html>
<html lang="en">
<head>
<meta charset="utf-8">
<title>Gullwind Stonecut Earthworks</title>
<link rel="stylesheet" href="https://fonts.googleapis.com/css2?family=Russo+One&family=Lexend:wght@400;500;600&display=swap">
<style>
:root{
  --lime:#cedb00;
  --ink:#0d0d0d;
  --white:#ffffff;
  --paper:#ffffff;
  --grey-bg:#e4e3e1;
  --footer:#262626;
  --field:#2f2f2f;
  --muted:#8a8a8a;
  --head:"Russo One", sans-serif;
  --body:"Lexend", sans-serif;
}
*{margin:0;padding:0;box-sizing:border-box}
html,body{width:1200px;height:2673px;overflow:hidden}
body{position:relative;background:var(--paper);font-family:var(--body);color:var(--ink)}
.abs{position:absolute}
.band{position:absolute;height:12px;background:var(--lime)}
.btn{position:absolute;display:flex;align-items:center;justify-content:center;font-family:var(--head);font-size:12px;letter-spacing:.3px;border-radius:3px}
.btn--dark{background:var(--ink);color:var(--white)}
.btn--light{background:var(--white);color:var(--ink)}

/* header & hero */
.hero{left:0;top:0;width:1200px;height:600px;background:linear-gradient(180deg,#3c3b38 0%,#6b6353 35%,#8c7556 62%,#5a4732 100%)}
.brand{display:flex;align-items:center;gap:10px;font-family:var(--body);font-weight:600;color:var(--white);font-size:24px;letter-spacing:.5px}
.brand__dot{width:30px;height:30px;background:var(--lime)}
.nav{left:500px;top:28px;display:flex;gap:31px;font-size:12px;font-weight:500;color:var(--white)}
.nav a{color:inherit;text-decoration:none}
.nav a.is-active{color:var(--lime);text-decoration:underline}
.hero__title{left:0;width:1200px;top:198px;text-align:center;font-family:var(--head);font-size:57px;line-height:57px;color:var(--white)}
.hero__title .lime{color:var(--lime)}

/* about */
.about__mark{left:228px;top:740px;width:320px;display:flex;flex-direction:column;align-items:center;gap:14px;font-family:var(--body);font-weight:600;font-size:34px;line-height:40px;text-align:center;color:var(--ink)}
.about__mark span.sq{width:60px;height:60px;background:var(--ink)}
.sec-title{font-family:var(--head);font-size:33px;display:flex;align-items:center;gap:14px}
.sec-title i{display:block;width:26px;height:1px;background:currentColor;opacity:.6}
.about__title{left:612px;top:690px;color:var(--lime)}
.about__lead{left:612px;top:750px;width:390px;font-size:15px;font-weight:500;line-height:20px}
.about__text{left:612px;top:802px;width:390px;font-size:11px;line-height:14px}

/* services */
.services{left:0;top:1035px;width:1200px;height:618px;background:linear-gradient(120deg,#ecebea 0%,#dcd8d2 45%,#e6e4e1 100%)}
.services__title{left:0;width:1200px;top:1115px;justify-content:center;color:var(--ink)}
.service{position:absolute;top:1177px;width:387px;height:324px;display:flex;align-items:flex-end;justify-content:center;padding-bottom:18px;color:var(--white);font-family:var(--body);font-weight:500;font-size:27px}
.service--excavator{left:194px;background:linear-gradient(180deg,#5f8fc4 0%,#a3b9cf 35%,#6b6a55 70%,#1b1b1b 100%)}
.service--earthworks{left:615px;background:linear-gradient(180deg,#6e9aa7 0%,#b4c1c2 35%,#6a5a3a 70%,#1a1714 100%)}

/* projects */
.projects__title{left:0;width:1200px;top:1745px;justify-content:center;color:var(--lime)}
.project__photo{position:absolute}
.project__cap{position:absolute;background:var(--white);font-size:15px;color:#555}
.project__cap--feature{padding:14px 18px}
.project__cap--feature h3{font-weight:500;font-size:15px;color:var(--lime)}
.project__cap--feature p{margin-top:6px;font-size:11px;line-height:15px;color:#777}

/* footer */
.footer{left:0;top:2318px;width:1200px;height:324px;background:var(--footer)}
.footer__brand{left:0;width:1200px;top:2366px;justify-content:center;font-size:27px}
.col-title{font-family:var(--head);font-size:14px;color:var(--lime)}
.contact-list{list-style:none;font-size:12px;color:var(--white)}
.contact-list li{display:flex;gap:9px;margin-bottom:11px;line-height:14px}
.contact-list svg{flex:none;margin-top:1px}
.links{list-style:none;font-size:12px;color:var(--white)}
.links li{margin-bottom:8px}
.links .is-active{color:var(--lime);text-decoration:underline}
.field{position:absolute;border:1px solid #4a4a4a;background:var(--field);color:#9a9a9a;font-size:11px;padding:10px 12px}
.submit{background:var(--ink);color:var(--white)}
.bottom-bar{left:0;top:2642px;width:1200px;height:31px;background:var(--lime);font-size:12px;color:#222}
.social{position:absolute;top:9px;width:12px;height:12px;background:#1f1f1f}
</style>
</head>
<body>

<!-- Header / hero -->
<div class="abs hero" role="img" aria-label="Photo of a yellow excavator digging at a building construction site"></div>
<div class="abs brand" style="left:82px;top:22px">
  <span class="brand__dot"></span>Gullwind Stonecut
</div>
<nav class="abs nav">
  <a class="is-active" href="#">HOME</a><a href="#">ABOUT US</a><a href="#">SERVICES</a><a href="#">PROJECTS</a><a href="#">CONTACT US</a>
</nav>
<div class="btn btn--light" style="left:988px;top:22px;width:130px;height:30px">QUICK INQUIRY</div>
<h1 class="abs hero__title">
  <span class="lime">EXCAVATOR</span> &amp;<br><span class="lime">EARTHWORKS</span><br>COMPANY
</h1>
<div class="btn btn--light" style="left:535px;top:391px;width:130px;height:30px">CONTACT NOW</div>
<div class="band" style="left:612px;top:600px;width:588px"></div>

<!-- About -->
<div class="abs about__mark"><span class="sq"></span>GULLWIND<br>STONECUT</div>
<h2 class="abs sec-title about__title">ABOUT US <i></i></h2>
<p class="abs about__lead">Lorem Ipsum Is Simply Dummy Text Of The Printing And Typesetting Industry.</p>
<p class="abs about__text">Lorem Ipsum Has Been The Industry's Standard Dummy Text Ever Since The 1500s, When An Unknown Printer Took A Galley Of Type And Scrambled It To Make A Type Specimen Book. It Has Survived Not Only Five Centuries, But Also The Leap Into Electronic Typesetting, Remaining Essentially Unchanged.</p>
<div class="btn btn--dark" style="left:612px;top:900px;width:112px;height:33px">READ MORE</div>
<div class="band" style="left:0;top:1022px;width:588px"></div>

<!-- Services -->
<div class="abs services" role="img" aria-label="Faded blurred photo of a construction site behind the services"></div>
<h2 class="abs sec-title services__title"><i></i>SERVICES<i></i></h2>
<div class="service service--excavator" role="img" aria-label="Photo of a yellow excavator in front of mountains">Excavator</div>
<div class="service service--earthworks" role="img" aria-label="Photo of a yellow bulldozer pushing soil">Earthworks</div>
<div class="btn btn--dark" style="left:535px;top:1533px;width:130px;height:33px">CONTACT NOW</div>
<div class="band" style="left:612px;top:1653px;width:588px"></div>

<!-- Projects -->
<h2 class="abs sec-title projects__title"><i></i>OUR PROJECTS<i></i></h2>

<div class="project__photo" style="left:0;top:1838px;width:356px;height:258px;background:linear-gradient(180deg,#d9742c 0%,#e8a355 30%,#8a4a2a 60%,#5a2e1b 100%)" role="img" aria-label="Photo of a worker beside a pipeline trench at sunset"></div>
<div class="project__cap" style="left:0;top:2096px;width:294px;height:27px;line-height:27px">Your title here</div>
<div class="abs" style="left:294px;top:2096px;width:62px;height:27px;background:#6e3a22"></div>

<div class="project__photo" style="left:381px;top:1807px;width:438px;height:347px;background:linear-gradient(180deg,#9aa3a8 0%,#c9cdcf 30%,#b3846a 60%,#8e4f31 100%)" role="img" aria-label="Photo of a yellow backhoe loader at a city construction site"></div>
<div class="project__cap project__cap--feature" style="left:443px;top:2085px;width:313px;height:69px">
  <h3>Your Title Here</h3>
  <p>Lorem Ipsum is dummy text of the printing &amp; typesetting industry.</p>
</div>

<div class="project__photo" style="left:844px;top:1838px;width:356px;height:258px;background:linear-gradient(180deg,#4a88c8 0%,#a7c4de 35%,#c9a587 65%,#b7835d 100%)" role="img" aria-label="Photo of a wheel loader moving sand near apartment blocks"></div>
<div class="abs" style="left:844px;top:2096px;width:62px;height:27px;background:#c49a74"></div>
<div class="project__cap" style="left:906px;top:2096px;width:294px;height:27px;line-height:27px;padding-left:18px">Your title here</div>

<div class="btn btn--dark" style="left:552px;top:2185px;width:98px;height:33px">VIEW ALL</div>
<div class="band" style="left:0;top:2306px;width:588px"></div>

<!-- Footer -->
<div class="abs footer" role="img" aria-label="Dark faded photo of an excavator on a construction site"></div>
<div class="abs brand footer__brand"><span class="brand__dot"></span>Gullwind Stonecut</div>

<h4 class="abs col-title" style="left:156px;top:2448px">CONTACT INFO</h4>
<ul class="abs contact-list" style="left:156px;top:2484px;width:230px">
  <li><svg width="11" height="11" viewBox="0 0 24 24"><path fill="#cedb00" d="M6.6 10.8a15 15 0 0 0 6.6 6.6l2.2-2.2a1 1 0 0 1 1-.25 11 11 0 0 0 3.6.6 1 1 0 0 1 1 1V20a1 1 0 0 1-1 1A17 17 0 0 1 3 4a1 1 0 0 1 1-1h3.5a1 1 0 0 1 1 1c0 1.25.2 2.45.6 3.6a1 1 0 0 1-.25 1z"/></svg>+61 400 555 218</li>
  <li><svg width="11" height="11" viewBox="0 0 24 24"><path fill="#cedb00" d="M2 5h20v14H2z"/><path fill="none" stroke="#262626" stroke-width="2" d="M2 5l10 8 10-8"/></svg>hello@gullwindstonecut.com.au</li>
  <li><svg width="11" height="13" viewBox="0 0 24 28"><path fill="#cedb00" d="M12 0a10 10 0 0 0-10 10c0 7.5 10 18 10 18s10-10.5 10-18A10 10 0 0 0 12 0zm0 14a4 4 0 1 1 0-8 4 4 0 0 1 0 8z"/></svg>14 Quarrystone Rd,<br>Kelmscott WA 6111,<br>Australia</li>
</ul>

<h4 class="abs col-title" style="left:405px;top:2448px">QUICK LINKS</h4>
<ul class="abs links" style="left:405px;top:2484px">
  <li class="is-active">Home</li><li>About Us</li><li>Services</li><li>Projects</li><li>Contact Us</li>
</ul>

<h4 class="abs col-title" style="left:586px;top:2448px">QUICK INQUIRY</h4>
<div class="field" style="left:586px;top:2482px;width:220px;height:32px">First Name</div>
<div class="field" style="left:586px;top:2520px;width:220px;height:32px">Email</div>
<div class="field" style="left:586px;top:2559px;width:220px;height:33px">Phone</div>
<div class="field" style="left:824px;top:2482px;width:220px;height:67px">How Can We Help?</div>
<div class="btn submit" style="left:824px;top:2559px;width:220px;height:33px">SUBMIT</div>

<div class="abs bottom-bar">
  <span class="abs" style="left:156px;top:8px">© 2026 Gullwind Stonecut Earthworks. All Right Reserved</span>
  <span class="abs" style="left:493px;top:8px">ABN: 12345678901</span>
  <span class="social" style="left:980px" aria-label="Social link"></span>
  <span class="social" style="left:1002px" aria-label="Social link"></span>
  <span class="social" style="left:1025px;top:6px;width:18px;height:18px;border-radius:50%;background:var(--white)" aria-label="Social link"></span>
</div>

</body>
</html>
```